Modern Business Card for Lanternfield 2018

Our company assumes the best about people. We are creating an online community of entrepreneurs and business leaders who struggle with marketing their business online.

This business card should POP! We recently got a new logo and are launching a new website next month, so our business cards should make a statement that feels:
-Fresh
-Smart
-Trustworthy
-Fun

Target Market(s)

small business owners, entrepreneurs

Industry/Entity Type

Digital Marketing

Contact Information for Business Card

Dimensions: 3.5" x 2"

Font styles to use
Sans Serif

Colors
f37122
ffffff

Requirements
Must have
• We need a business card with a modern, bold design. We will use one side of the card as a lead-generation offer, so text on one side will need to fit up to 140 characters. The business card should stick to our core colors (orange, black, and white).
Nice to have
• We think a vertical "portrait" design could be interesting.
Should not have
• Should not look like a traditional business card. The round icon should stand out from a distance.

```html
<!DOCTYPE html>
<html lang="en">
<head>
<meta charset="utf-8">
<title>Lanternfield Business Card</title>
<link href="https://fonts.googleapis.com/css2?family=Montserrat:wght@800&family=Oswald:wght@500&family=Work+Sans:wght@400;500&family=Roboto:wght@400&display=swap" rel="stylesheet">
<style>
  :root {
    --orange: #f37122;
    --white: #ffffff;
    --card: #1c1c1d;
    --card-edge: #242425;
    --backdrop: #2a2a2b;
    --muted: #e8e8e8;
  }
  * { margin: 0; padding: 0; box-sizing: border-box; }
  html, body {
    width: 1200px; height: 900px; overflow: hidden;
    background: var(--backdrop);
  }
  .canvas {
    position: relative; width: 1200px; height: 900px;
    display: flex; flex-direction: column; align-items: center; justify-content: center; gap: 24px;
  }
  .card {
    position: relative; width: 700px; height: 400px;
    background: linear-gradient(135deg, var(--card-edge), var(--card) 60%);
    border-bottom: 6px solid var(--orange);
    box-shadow: 0 10px 24px rgba(0,0,0,0.45);
    color: var(--white);
    overflow: hidden;
  }

  /* Front */
  .card--front { text-align: center; }
  .brand {
    position: absolute; top: 52px; left: 0; right: 0;
    display: flex; flex-direction: column; align-items: center; gap: 18px;
  }
  .brand__dot {
    width: 58px; height: 58px; border-radius: 50%; background: var(--orange);
  }
  .brand__name {
    font-family: "Montserrat", sans-serif; font-weight: 800;
    font-size: 56px; letter-spacing: 3px; color: var(--white);
  }
  .offer {
    position: absolute; top: 248px; left: 0; right: 0;
    font-family: "Work Sans", sans-serif; font-size: 14px; line-height: 1.45; color: var(--muted);
  }
  .front__rule {
    position: absolute; top: 308px; left: 90px; right: 90px;
    height: 1px; background: rgba(243,113,34,0.45);
  }
  .tagline {
    position: absolute; top: 326px; left: 0; right: 0;
    font-family: "Roboto", sans-serif; font-size: 17px; letter-spacing: 1px; color: var(--white);
  }

  /* Back */
  .person {
    position: absolute; top: 136px; left: 76px;
    display: flex; flex-direction: column; align-items: flex-end;
  }
  .person__name {
    font-family: "Oswald", sans-serif; font-weight: 500; font-size: 38px;
    letter-spacing: 1px; color: var(--orange); line-height: 1.1;
    text-transform: uppercase; white-space: nowrap;
  }
  .person__role {
    font-family: "Work Sans", sans-serif; font-size: 16px; letter-spacing: 1px;
    color: var(--white); white-space: nowrap;
  }
  .back__divider {
    position: absolute; top: 140px; left: 356px; width: 2px; height: 58px; background: var(--white);
  }
  .contacts {
    position: absolute; top: 131px; left: 380px; list-style: none;
    font-family: "Work Sans", sans-serif; font-size: 17px; letter-spacing: 0.4px; color: var(--white);
  }
  .contacts li { display: flex; align-items: center; gap: 9px; line-height: 1.45; white-space: nowrap; }
  .contacts svg { width: 12px; height: 12px; flex: none; }
  .contacts .accent { color: var(--orange); }
  .address {
    position: absolute; bottom: 48px; left: 76px;
    font-family: "Work Sans", sans-serif; font-size: 18px; letter-spacing: 1px; color: var(--white);
    white-space: nowrap;
  }
</style>
</head>
<body>
<main class="canvas">

  <section class="card card--front">
    <div class="brand">
      <span class="brand__dot"></span>
      <span class="brand__name">LANTERNFIELD</span>
    </div>
    <p class="offer">Get your free Lanternfield<br>Starter Package and our marketing guide today at</p>
    <div class="front__rule"></div>
    <p class="tagline">REACH MORE PEOPLE. MAKE MORE MONEY. CREATE MORE IMPACT.</p>
  </section>

  <section class="card card--back">
    <div class="person">
      <h1 class="person__name">Dana Whitford</h1>
      <p class="person__role">Story Marketing Coach</p>
    </div>
    <div class="back__divider"></div>
    <ul class="contacts">
      <li>
        <svg viewBox="0 0 24 24" aria-hidden="true"><path fill="#f37122" d="M6.6 10.8a15.1 15.1 0 0 0 6.6 6.6l2.2-2.2a1 1 0 0 1 1-.25 11.4 11.4 0 0 0 3.6.57 1 1 0 0 1 1 1V20a1 1 0 0 1-1 1A17 17 0 0 1 3 4a1 1 0 0 1 1-1h3.5a1 1 0 0 1 1 1c0 1.250.2 2.45.57 3.57a1 1 0 0 1-.25 1z"/></svg>
        (555) 014-2870
      </li>
      <li>
        <svg viewBox="0 0 24 24" aria-hidden="true"><rect x="2.5" y="5" width="19" height="14" rx="1.5" fill="none" stroke="#f37122" stroke-width="2"/><path d="M3 6l9 7 9-7" fill="none" stroke="#f37122" stroke-width="2"/></svg>
        Dana@lanternfieldnow.com
      </li>
      <li>
        <svg viewBox="0 0 24 24" aria-hidden="true"><g fill="none" stroke="#f37122" stroke-width="2"><circle cx="12" cy="12" r="9.5"/><ellipse cx="12" cy="12" rx="4" ry="9.5"/><path d="M2.5 12h19"/></g></svg>
        <span>www.<span class="accent">lanternfieldnow</span>.com</span>
      </li>
    </ul>
    <p class="address">ZX2040 , 18/3 Harbor Lane, Eastvale city, Northland</p>
  </section>

</main>
</body>
</html>
```